Stationery for use with Vellmar reports

I would like to get a stationery design that my firm -- Vellmar Partners -- will use as a format for reports that we send our clients. I am specifically looking for a design for use on a piece of paper or letterhead -- not business cards or envelopes.

We are an Africa based US risk intelligence and strategy firm that works with multinational corporations operating in West Africa. Our initial thinking is that we would like a color scheme consistent with our existing logo -- however we are open to other color schemes.

Also, we would like to see at least two separate versions: one with our company name and logo, the other without name and logo.

We also would like font recommendations for the stationary design.

The final design should communicate discreet professionalism and a modern approach, but it should not overshadow the words and information printed on the stationery.

Target Market(s)

Multinational corporations that currently use our products.

Font styles to use
Serif
Sans Serif

Requirements
Must have
• Sense of discreet professionalism that will not overshadow the content we put onto the stationery format.
• We would like to see designs with and without our company name/logo.
• Please suggest fonts that would work with the stationery.
Nice to have
• Ideally colors consistent with out existing logo, though we are open to and even encourage other ideas.
Should not have
• No need for business cards or envelopes.

```html
<!DOCTYPE html>
<html lang="en">
<head>
<meta charset="utf-8">
<title>Vellmar Partners — Report Letterhead</title>
<link rel="stylesheet" href="https://fonts.googleapis.com/css2?family=Montserrat:wght@500;700&display=swap">
<style>
  :root {
    --paper: #f3f0ea;
    --ink-navy: #1f3b4d;
    --rule-gold: #b57a2c;
    --mark-gold: #e0a94f;
    --faint-gold: rgba(224, 169, 79, 0.16);
  }
  * { margin: 0; padding: 0; box-sizing: border-box; }
  html, body {
    width: 849px;
    height: 1200px;
    overflow: hidden;
    background: var(--paper);
  }
  .letterhead {
    position: relative;
    width: 849px;
    height: 1200px;
    background: var(--paper);
    font-family: "Montserrat", sans-serif;
  }
  .brand-square {
    position: absolute;
    left: 52px;
    top: 44px;
    width: 92px;
    height: 92px;
    background: var(--mark-gold);
  }
  .brand-name {
    position: absolute;
    right: 33px;
    top: 68px;
    text-align: right;
    color: var(--ink-navy);
    font-weight: 700;
    line-height: 1;
  }
  .brand-name .primary {
    display: block;
    font-size: 36px;
    letter-spacing: 1px;
  }
  .brand-name .secondary {
    display: block;
    margin-top: 8px;
    font-size: 17px;
    letter-spacing: 4px;
  }
  .header-rule {
    position: absolute;
    left: 160px;
    top: 145px;
    width: 666px;
    height: 3px;
    background: var(--rule-gold);
  }
  .background-name {
    position: absolute;
    left: 0;
    top: 540px;
    width: 100%;
    text-align: center;
    color: var(--faint-gold);
    font-weight: 700;
    font-size: 104px;
    letter-spacing: 4px;
    line-height: 1;
  }
</style>
</head>
<body>
  <main class="letterhead">
    <div class="brand-square" aria-hidden="true"></div>
    <div class="brand-name">
      <span class="primary">VELLMAR</span>
      <span class="secondary">PARTNERS</span>
    </div>
    <div class="header-rule" aria-hidden="true"></div>
    <div class="background-name" aria-hidden="true">VELLMAR</div>
  </main>
</body>
</html>
```